Visitenkarten-Design für Persisches Restaurant
Zielgruppe
persisches Restaurant, suche ein Hochwertiges Design für internationale Kunden
Aufgabenstellung
möchte eine hochwertige und elegante visitenkarte
auf der Vorderseite sollte das Logo sein und auf der Rückseite Öffnungszeit, Adresse, Tel. E-Mail und homepage

```html
<!DOCTYPE html>
<html lang="de">
<head>
<meta charset="utf-8">
<title>Darvana – Visitenkarte</title>
<link href="https://fonts.googleapis.com/css2?family=Cinzel:wght@500&family=Work+Sans:wght@400&display=swap" rel="stylesheet">
<style>
  :root {
    --backdrop: #e3e3e3;
    --card: #fbfbfa;
    --ink: #1c1c1c;
    --ink-soft: #6a6a6a;
    --rule: #2a2a2a;
  }
  * { margin: 0; padding: 0; box-sizing: border-box; }
  html, body { width: 1200px; height: 857px; overflow: hidden; }
  body {
    background: var(--backdrop);
    display: flex;
    align-items: center;
    justify-content: center;
    gap: 60px;
    font-family: "Work Sans", Arial, sans-serif;
    color: var(--ink);
  }
  .card {
    position: relative;
    width: 520px;
    height: 340px;
    background: var(--card);
    box-shadow: 0 2px 10px rgba(0,0,0,0.08);
  }

  /* Front */
  .card--front {
    display: flex;
    align-items: center;
    justify-content: center;
  }
  .lockup { text-align: center; }
  .lockup__name {
    display: flex;
    align-items: center;
    justify-content: center;
    gap: 12px;
    font-family: "Cinzel", Georgia, serif;
    font-weight: 500;
    font-size: 44px;
    letter-spacing: 2px;
    color: var(--ink);
    line-height: 1;
  }
  .lockup__dot {
    width: 14px;
    height: 14px;
    border-radius: 50%;
    background: var(--ink);
  }
  .lockup__tagline {
    margin-top: 8px;
    padding-top: 6px;
    border-top: 1px solid var(--rule);
    font-size: 11px;
    letter-spacing: 3.2px;
    color: var(--ink-soft);
  }
  .lockup__since {
    margin-top: 3px;
    font-size: 7px;
    letter-spacing: 2px;
    color: var(--ink-soft);
  }

  /* Back */
  .back__mark {
    position: absolute;
    left: 46px;
    top: 56px;
    font-family: "Cinzel", Georgia, serif;
    font-weight: 500;
    font-size: 26px;
    letter-spacing: 1px;
    color: var(--ink);
  }
  .contact {
    position: absolute;
    left: 290px;
    right: 0;
    top: 140px;
    font-size: 12px;
    letter-spacing: 1.2px;
    line-height: 1.45;
  }
  .contact__address { padding-right: 20px; }
  .contact__rule {
    margin: 8px 0 10px;
    border: 0;
    border-top: 1px solid var(--rule);
  }
  .contact__web { font-size: 12px; }
</style>
</head>
<body>
  <section class="card card--front" aria-label="Vorderseite">
    <div class="lockup">
      <div class="lockup__name"><span class="lockup__dot"></span>DARVANA</div>
      <div class="lockup__tagline">PERSISCHES RESTAURANT</div>
      <div class="lockup__since">SINCE 1999</div>
    </div>
  </section>

  <section class="card card--back" aria-label="Rückseite">
    <div class="back__mark">Darvana</div>
    <div class="contact">
      <p class="contact__address">Rosmarinweg 7, 60389<br>Frankfurt am Main, Germany<br>+49 69 000482</p>
      <hr class="contact__rule">
      <p class="contact__web">tafelbote.de</p>
    </div>
  </section>
</body>
</html>
```